Service vs Service Timeline Design

We need a graphic designed to show the difference between our service and another service. We have a wireframe of the "timeline" between the services to give you an idea of what the graphic design will need to look like. You will have some creative ability to make it was better then the wireframe, that is titled "wireframe". There are pictures of our mobile app attached as well for you to get a feel for our design. If this graphic goes well, we have another graphic in the pipeline. Our website is: https://www.quoddle.com. We are in the process of building a website that better matches the design of our app right now.
It Service

```html
<!DOCTYPE html>
<html lang="en">
<head>
<meta charset="utf-8">
<title>Why We're Better Than Others?</title>
<link href="https://fonts.googleapis.com/css2?family=Libre+Baskerville&family=Roboto:wght@400;500;700&display=swap" rel="stylesheet">
<style>
  :root {
    --header-bg: #3d4242;
    --ours-bg: #5cd6a8;
    --theirs-bg: #e8e8e8;
    --ink: #2f3535;
    --badge: #ffe51a;
    --badge-edge: #e6c800;
    --vs-blue: #0b57b0;
    --footer-red: #f50000;
    --white: #ffffff;
  }
  html, body { margin: 0; padding: 0; overflow: hidden; background: var(--white); }
  .canvas {
    position: relative; width: 1062px; height: 1200px; overflow: hidden;
    background: var(--white); font-family: "Roboto", Arial, sans-serif; color: var(--ink);
  }
  .header {
    position: absolute; left: 25px; top: 22px; width: 1012px; height: 143px;
    background: var(--header-bg);
  }
  .header__title {
    position: absolute; left: 0; right: 0; top: 48px; margin: 0; text-align: center;
    font-family: "Libre Baskerville", Georgia, serif; font-weight: 400; font-size: 41px;
    color: var(--white); letter-spacing: 0.3px;
  }
  .header__rule {
    position: absolute; left: 478px; top: 113px; width: 100px; height: 1px; background: #8c9191;
  }
  .panel { position: absolute; top: 165px; height: 922px; }
  .panel--ours { left: 25px; width: 506px; background: var(--ours-bg); }
  .panel--theirs { left: 531px; width: 506px; background: var(--theirs-bg); }
  .panel__name {
    position: absolute; top: 237px; transform: translate(-50%, -50%);
    margin: 0; font-size: 36px; font-weight: 700; color: #3a4040;
  }
  .panel__rule { position: absolute; top: 271px; height: 2px; background: var(--ink); }
  .vs {
    position: absolute; left: 475px; top: 179px; width: 104px; height: 104px; border-radius: 50%;
    background: var(--vs-blue); border: 4px solid var(--white); box-shadow: 0 0 0 2px var(--vs-blue);
    display: flex; align-items: center; justify-content: center;
    color: var(--white); font-weight: 700; font-size: 32px;
  }
  .order {
    position: absolute; top: 331px; transform: translateY(-50%);
    display: flex; align-items: center; gap: 16px;
    font-size: 22px; font-weight: 700; color: var(--ink);
  }
  .step {
    position: absolute; transform: translate(-50%, -50%); text-align: center;
    font-size: 17px; line-height: 22px; white-space: nowrap; color: var(--ink);
  }
  .step b { font-weight: 700; }
  .step--lead { font-size: 17px; line-height: 22px; }
  .arrow { position: absolute; transform: translate(-50%, -50%); width: 14px; height: 26px; }
  .date {
    position: absolute; transform: translateY(-50%);
    width: 60px; height: 40px; box-sizing: border-box;
    background: var(--badge); border: 1px solid var(--badge-edge); border-radius: 4px;
    display: flex; align-items: center; justify-content: center;
    font-size: 16px; font-weight: 700; color: #333;
  }
  .date--wide { width: 113px; }
  .date sup { font-size: 10px; margin-left: 1px; }
  .footer {
    position: absolute; left: 25px; top: 1087px; width: 1012px; height: 84px;
    background: var(--footer-red); color: var(--white); font-weight: 700; font-size: 27px;
  }
  .footer__total { position: absolute; top: 50%; transform: translate(-50%, -50%); white-space: nowrap; }
</style>
</head>
<body>
<main class="canvas">
  <header class="header">
    <h1 class="header__title">Why We’re Better Than Others?</h1>
    <div class="header__rule"></div>
  </header>

  <section class="panel panel--ours" aria-label="Quoddle timeline"></section>
  <section class="panel panel--theirs" aria-label="Bins timeline"></section>

  <h2 class="panel__name" style="left:277px">Quoddle</h2>
  <div class="panel__rule" style="left:56px;width:422px"></div>
  <h2 class="panel__name" style="left:785px">Bins</h2>
  <div class="panel__rule" style="left:587px;width:423px"></div>
  <div class="vs">VS.</div>

  <!-- Quoddle column -->
  <div class="order" style="left:94px">
    <svg width="26" height="40" viewBox="0 0 26 40" aria-hidden="true"><rect x="2" y="2" width="22" height="36" rx="4" fill="none" stroke="#2f3535" stroke-width="3"/><rect x="7" y="8" width="12" height="22" fill="none" stroke="#2f3535" stroke-width="1.5"/><circle cx="13" cy="34" r="1.8" fill="#2f3535"/></svg>
    <span>ORDER ANYWHERE</span>
  </div>
  <div class="date" style="left:405px;top:331px">7<sup>th</sup></div>

  <svg class="arrow" style="left:262px;top:374px" viewBox="0 0 14 26"><rect x="5.5" y="0" width="3" height="17" fill="#2f3535"/><path d="M0 15h14L7 26z" fill="#2f3535"/></svg>
  <div class="step" style="left:262px;top:440px">“We’ll drop it next<br><b>Tuesday the 14<sup style="font-size:9px">th</sup>”</b></div>
  <div class="date" style="left:405px;top:441px">14<sup>th</sup></div>

  <svg class="arrow" style="left:262px;top:504px" viewBox="0 0 14 26"><rect x="5.5" y="0" width="3" height="17" fill="#2f3535"/><path d="M0 15h14L7 26z" fill="#2f3535"/></svg>
  <div class="step" style="left:262px;top:584px">TuesDay The 14th Removal<br>Partner on the way<br><b>Call Time Updates</b></div>
  <div class="date" style="left:405px;top:573px">14<sup>th</sup></div>

  <svg class="arrow" style="left:262px;top:682px" viewBox="0 0 14 26"><rect x="5.5" y="0" width="3" height="17" fill="#2f3535"/><path d="M0 15h14L7 26z" fill="#2f3535"/></svg>
  <div class="step" style="left:262px;top:746px">Removal Partners load<br><b>Trailer Quickly</b></div>
  <div class="date" style="left:405px;top:746px">14<sup>th</sup></div>

  <svg class="arrow" style="left:262px;top:800px" viewBox="0 0 14 26"><rect x="5.5" y="0" width="3" height="17" fill="#2f3535"/><path d="M0 15h14L7 26z" fill="#2f3535"/></svg>
  <div class="step" style="left:262px;top:858px">Junk gone<br><b>Faster</b></div>
  <div class="date" style="left:405px;top:862px">14<sup>th</sup></div>

  <svg class="arrow" style="left:262px;top:914px" viewBox="0 0 14 26"><rect x="5.5" y="0" width="3" height="17" fill="#2f3535"/><path d="M0 15h14L7 26z" fill="#2f3535"/></svg>
  <div class="step" style="left:262px;top:988px"><b>Feedback is easy<br>Fast improvements<br>Best workers determined</b></div>
  <div class="date" style="left:405px;top:968px">14<sup>th</sup></div>

  <svg class="arrow" style="left:262px;top:1046px" viewBox="0 0 14 26"><rect x="5.5" y="0" width="3" height="17" fill="#2f3535"/><path d="M0 15h14L7 26z" fill="#2f3535"/></svg>

  <!-- Bins column -->
  <div class="order" style="left:582px">
    <svg width="44" height="36" viewBox="0 0 44 36" aria-hidden="true"><rect x="6" y="3" width="32" height="24" rx="2" fill="none" stroke="#2f3535" stroke-width="3.5"/><rect x="1" y="29" width="42" height="5" rx="1.5" fill="#2f3535"/></svg>
    <span>ORDER ONLINE</span>
  </div>
  <div class="date" style="left:914px;top:330px">7<sup>th</sup></div>

  <svg class="arrow" style="left:766px;top:373px" viewBox="0 0 14 26"><rect x="5.5" y="0" width="3" height="17" fill="#2f3535"/><path d="M0 15h14L7 26z" fill="#2f3535"/></svg>
  <div class="step" style="left:766px;top:424px">“We’ll drop it next<br><b>Tuesday the 14<sup style="font-size:9px">th</sup>”</b></div>
  <div class="date" style="left:914px;top:425px">14<sup>th</sup></div>

  <svg class="arrow" style="left:766px;top:479px" viewBox="0 0 14 26"><rect x="5.5" y="0" width="3" height="17" fill="#2f3535"/><path d="M0 15h14L7 26z" fill="#2f3535"/></svg>
  <div class="step" style="left:766px;top:527px">Bin arrives<br><b>Wednesday</b></div>
  <div class="date" style="left:914px;top:531px">15<sup>th</sup></div>

  <svg class="arrow" style="left:766px;top:584px" viewBox="0 0 14 26"><rect x="5.5" y="0" width="3" height="17" fill="#2f3535"/><path d="M0 15h14L7 26z" fill="#2f3535"/></svg>
  <div class="step" style="left:766px;top:635px">You Load bin for<br><b>One Week</b></div>
  <div class="date date--wide" style="left:887px;top:626px">15<sup>th</sup>&nbsp;-&nbsp;21<sup>st</sup></div>

  <svg class="arrow" style="left:766px;top:701px" viewBox="0 0 14 26"><rect x="5.5" y="0" width="3" height="17" fill="#2f3535"/><path d="M0 15h14L7 26z" fill="#2f3535"/></svg>
  <div class="step" style="left:766px;top:750px">Call to pickup<br><b>Bin</b></div>
  <div class="date" style="left:914px;top:734px">21<sup>st</sup></div>

  <svg class="arrow" style="left:766px;top:809px" viewBox="0 0 14 26"><rect x="5.5" y="0" width="3" height="17" fill="#2f3535"/><path d="M0 15h14L7 26z" fill="#2f3535"/></svg>
  <div class="step" style="left:766px;top:869px">Pickup Bin<br><b>Wednesday</b><br>(next week)</div>
  <div class="date" style="left:914px;top:851px">22<sup>nd</sup></div>

  <svg class="arrow" style="left:766px;top:925px" viewBox="0 0 14 26"><rect x="5.5" y="0" width="3" height="17" fill="#2f3535"/><path d="M0 15h14L7 26z" fill="#2f3535"/></svg>
  <div class="step" style="left:766px;top:993px"><b>No easy feedback<br>Slow Improvements<br>Years to get the best workers</b></div>
  <div class="date" style="left:914px;top:1009px">22<sup>nd</sup></div>

  <svg class="arrow" style="left:766px;top:1050px" viewBox="0 0 14 26"><rect x="5.5" y="0" width="3" height="17" fill="#2f3535"/><path d="M0 15h14L7 26z" fill="#2f3535"/></svg>

  <footer class="footer">
    <span class="footer__total" style="left:252px">Total Removal Time: 1-3 hrs</span>
    <span class="footer__total" style="left:760px">Total Removal timeline : 8 days</span>
  </footer>
</main>
</body>
</html>
```